Fish guide business card

Buisiness card

Target Market(s)

Visitors to Gull Harbour BC wanting to catch fish in the ocean and have a memorable adventure fun filled day

Industry/Entity Type

Tourism

Contact Information for Business Card

Phone number 250 318 two cards Ray 250 318 7262 other card Lou 250 6093714 both have email info@lwgullrocktours.com and website www.lwgullrocktours.com

Requirements
Must have
• Email, website , name , phone , logo , Gull Harbour BC
Nice to have
• Uploaded pictures have boat and man with fish picture

```html
<!DOCTYPE html>
<html lang="en">
<head>
<meta charset="utf-8">
<title>LW Gull Rock Tours – Business Card</title>
<link href="https://fonts.googleapis.com/css2?family=Montserrat:wght@400;500;700;800&display=swap" rel="stylesheet">
<style>
  :root {
    --navy: #1c1760;
    --navy-deep: #0d0a3a;
    --white: #ffffff;
    --paper: #f4f4f7;
    --ink: #2b2a55;
    --rule: #a9a9b8;
    --backdrop: #e6e3de;
    --photo-sky: #8fb8d8;
    --photo-water: #2f7da6;
    --photo-forest: #1f5a48;
    --accent-band: #dcdcec;
  }
  * { margin: 0; padding: 0; box-sizing: border-box; }
  html, body { width: 1200px; height: 900px; overflow: hidden; }
  body {
    background: var(--backdrop);
    font-family: "Montserrat", sans-serif;
    display: flex;
    flex-direction: column;
    align-items: center;
    justify-content: center;
    gap: 24px;
  }
  .card {
    width: 760px;
    height: 420px;
    border-radius: 30px;
    overflow: hidden;
    background: linear-gradient(160deg, var(--white), var(--paper));
    box-shadow: 0 10px 28px rgba(0,0,0,0.18);
  }
  .card svg { display: block; width: 100%; height: 100%; }
  .brand-name { font-family: "Montserrat", sans-serif; font-weight: 800; font-size: 14px; }
  .web-arc { font-family: "Montserrat", sans-serif; font-weight: 700; font-size: 20px; letter-spacing: 6px; fill: var(--navy); }
  .contact-name { font-family: "Montserrat", sans-serif; font-weight: 800; font-size: 30px; fill: var(--navy); }
  .contact-line { font-family: "Montserrat", sans-serif; font-weight: 500; font-size: 20px; fill: var(--ink); }
</style>
</head>
<body>

  <section class="card card-front">
    <svg viewBox="0 0 760 420" xmlns="http://www.w3.org/2000/svg">
      <defs>
        <linearGradient id="photoTone" x1="0" y1="1" x2="1" y2="0">
          <stop offset="0" stop-color="var(--photo-forest)"/>
          <stop offset="0.35" stop-color="var(--photo-water)"/>
          <stop offset="0.6" stop-color="var(--photo-sky)"/>
          <stop offset="1" stop-color="var(--photo-forest)"/>
        </linearGradient>
        <path id="frontTextArc" d="M170,388 C280,305 480,205 740,178"/>
      </defs>

      <path class="front-photo" role="img" aria-label="Photo of an angler fishing from rocks on a forest-lined lake"
            d="M0,0 H760 V140 C460,170 200,300 40,420 H0 Z" fill="url(#photoTone)"/>

      <path class="rod-and-fish-band" role="img" aria-label="Illustration of an orca, fishing rod and salmon along the curve"
            d="M40,410 C200,292 460,166 750,136" fill="none" stroke="var(--navy)" stroke-width="20" stroke-linecap="round"/>

      <text class="web-arc"><textPath href="#frontTextArc">www.lwgullrocktours.com</textPath></text>

      <g class="front-logo">
        <circle cx="610" cy="78" r="64" fill="none" stroke="var(--white)" stroke-width="5"/>
        <text class="brand-name" x="610" y="74" text-anchor="middle" fill="var(--white)">LW Gull Rock</text>
        <text class="brand-name" x="610" y="93" text-anchor="middle" fill="var(--white)">Tours</text>
      </g>
    </svg>
  </section>

  <section class="card card-back">
    <svg viewBox="0 0 760 420" xmlns="http://www.w3.org/2000/svg">
      <defs>
        <linearGradient id="navyTone" x1="0" y1="0" x2="1" y2="1">
          <stop offset="0" stop-color="var(--navy)"/>
          <stop offset="1" stop-color="var(--navy-deep)"/>
        </linearGradient>
      </defs>

      <path class="back-band" d="M0,0 H760 V110 C450,150 200,230 0,250 Z" fill="url(#navyTone)"/>

      <path class="rod-and-fish-band" role="img" aria-label="Illustration of an orca, fishing rod and salmon along the curve"
            d="M10,246 C200,226 450,146 750,110" fill="none" stroke="var(--accent-band)" stroke-width="18" stroke-linecap="round"/>

      <g class="back-logo">
        <circle cx="240" cy="330" r="70" fill="none" stroke="var(--navy)" stroke-width="6"/>
        <text class="brand-name" x="240" y="326" text-anchor="middle" fill="var(--navy)">LW Gull Rock</text>
        <text class="brand-name" x="240" y="345" text-anchor="middle" fill="var(--navy)">Tours</text>
      </g>

      <line class="divider" x1="350" y1="230" x2="350" y2="400" stroke="var(--rule)" stroke-width="1.5"/>

      <g class="contact">
        <text class="contact-name" x="380" y="258">LOU</text>

        <g class="icon-phone" transform="translate(390,294)">
          <circle r="11" fill="var(--navy)"/>
          <path d="M-4,-5 l3,0 l1,3 l-2,1 a6,6 0 0 0 3,3 l1,-2 l3,1 l0,3 a1,1 0 0 1 -1,1 a10,10 0 0 1 -9,-9 a1,1 0 0 1 1,-1 z" fill="var(--white)"/>
        </g>
        <text class="contact-line" x="410" y="301">250 609 3714</text>

        <g class="icon-pin" transform="translate(390,326)">
          <circle r="11" fill="var(--navy)"/>
          <path d="M0,7 C-5,1 -5,-2 -5,-2 a5,5 0 0 1 10,0 c0,0 0,3 -5,9 z" fill="var(--white)"/>
          <circle cy="-2" r="2" fill="var(--navy)"/>
        </g>
        <text class="contact-line" x="410" y="333">Gull Harbour BC</text>

        <g class="icon-mail" transform="translate(390,358)">
          <circle r="11" fill="var(--navy)"/>
          <rect x="-6" y="-4" width="12" height="8" rx="1" fill="var(--white)"/>
          <path d="M-6,-4 L0,1 L6,-4" fill="none" stroke="var(--navy)" stroke-width="1.2"/>
        </g>
        <text class="contact-line" x="410" y="365">info@lwgullrocktours.com</text>

        <g class="icon-web" transform="translate(390,390)">
          <circle r="11" fill="var(--navy)"/>
          <circle r="6" fill="none" stroke="var(--white)" stroke-width="1.4"/>
          <path d="M-6,0 H6 M0,-6 C-3,-2 -3,2 0,6 M0,-6 C3,-2 3,2 0,6" fill="none" stroke="var(--white)" stroke-width="1.2"/>
        </g>
        <text class="contact-line" x="410" y="397">www.lwgullrocktours.com</text>
      </g>
    </svg>
  </section>

</body>
</html>
```